Pixel Loft Gigs website

Our business is a freelance marketplace for IT and Digital contractors. It will provide a way for companies to take advantage of specialist talent for small periods of time and engage with them on a flexible basis. Logo should be something that shows Knowledge, Agility, Unlocking. Modern, simple, genius.We are looking for a site that conveys three things:- To have great technology you need great software, great hardware and great people. No one argues with that. To spend your dollars wisely and to focus on your core business, you have Cloud software and Cloud Hardware. Are any of your people in the cloud?- 5 specialists for the cost of one generalist- Cloud, agile and communication are converging to make the business case for remote specialists irresistible, we can get you the people you need to get your projects done, today.

Target Market(s)

Businesses, Tech professionals, Sales People, Recruiters

Industry/Entity Type

Information Technology

Logo Text

PixelLoftGigs or PLG

Coding

Coded - Design and coding required

Number of Pages Required

5+ page

Font styles to use
Sans Serif

Colors

Designer to choose colors to be used in the design.

Requirements
Must have
• A beautiful landing page with a technical feel to it
• a nice slick graphic for the How it works...
• A look and feel that is consistent throughout
• Some moving text
Should not have
• ugly anything

```html
<!DOCTYPE html>
<html lang="en">
<head>
<meta charset="utf-8">
<title>Pixel Loft Gigs — Freelance Marketplace</title>
<link href="https://fonts.googleapis.com/css2?family=Roboto:wght@300;400;500;700;900&display=swap" rel="stylesheet">
<style>
:root{
  --coral:#f7624f;
  --coral-soft:#ff8a6b;
  --peach:#fdeae6;
  --blush:#fff3f0;
  --ink:#1f2230;
  --text:#6f7280;
  --muted:#a4a7b0;
  --white:#ffffff;
  --orange:#f28a1c;
  --ring:#e8e8ec;
}
*{box-sizing:border-box;margin:0;padding:0}
html,body{width:1200px;height:3660px;overflow:hidden}
body{font-family:'Roboto',sans-serif;color:var(--ink);background:var(--white);position:relative}
.abs{position:absolute}
.btn{display:inline-block;background:linear-gradient(90deg,var(--coral),var(--coral-soft));color:var(--white);font-size:13px;font-weight:500;padding:15px 30px;border-radius:26px;box-shadow:0 8px 18px rgba(247,98,79,.35)}
p.copy{font-size:14px;line-height:24px;color:var(--text)}

/* header */
.hero-blob{left:420px;top:0;width:780px;height:560px}
.brand{left:60px;top:28px;display:flex;align-items:center;gap:12px}
.brand-mark{width:34px;height:34px;border-radius:50%;background:var(--coral)}
.brand-name{font-size:22px;font-weight:700;color:var(--coral)}
.nav{right:60px;top:26px;display:flex;gap:46px;align-items:center;font-size:13px;color:var(--white)}
.nav .pill{border:1.5px solid var(--white);border-radius:18px;padding:8px 18px}
.hero-title{left:60px;top:160px;font-size:50px;line-height:58px;font-weight:700}
.hero-title span{color:var(--coral)}
.hero-copy{left:60px;top:332px;width:400px;font-size:16px;line-height:26px;color:var(--text)}
.hero-btn{left:60px;top:470px}
.hero-art{left:690px;top:70px;width:460px;height:460px;border-radius:40px;background:linear-gradient(150deg,#cfd4ff,#7f86e6 55%,#ff9f87)}

/* roles */
.section-title{width:100%;text-align:center;font-size:34px;font-weight:700}
.roles{left:140px;top:700px;display:flex;gap:42px}
.role{width:276px;height:350px;background:var(--white);border-radius:24px;box-shadow:8px 10px 0 var(--coral),0 10px 30px rgba(0,0,0,.08);text-align:center;padding:36px 30px}
.role-figure{width:100px;height:100px;margin:0 auto 22px;border-radius:50%;background:linear-gradient(160deg,#ffd3c9,#f7624f)}
.role h3{font-size:18px;font-weight:500;margin-bottom:16px}
.role p{font-size:12px;line-height:21px;color:var(--muted)}

/* how it works */
.step-label{font-size:13px;color:var(--coral);margin-bottom:12px}
.step h3{font-size:24px;font-weight:500;line-height:32px;margin-bottom:18px}
.step p{width:440px;margin-bottom:28px}
.step-art{border:2px solid #f6c9c0;background:var(--white);padding:22px}
.step-art div{width:100%;height:100%;border-radius:6px}
.band{left:0;top:1600px;width:1200px;height:440px;background:var(--peach)}

/* stats */
.stats{left:150px;top:2440px;display:flex;gap:108px}
.stat{width:240px;text-align:center}
.stat svg{width:240px;height:240px}
.stat-num{font-size:46px;font-weight:500;fill:var(--ink);font-family:'Roboto',sans-serif}
.stat h4{margin-top:22px;font-size:15px;font-weight:500;line-height:22px;text-transform:uppercase}

/* testimonial */
.testi-band{left:0;top:2930px;width:1200px;height:400px;background:var(--peach)}
.testi-photo{left:80px;top:2960px;width:420px;height:340px;background:linear-gradient(140deg,#d8dee8,#8b95a8 60%,#5b6478)}
.play{left:262px;top:3102px;width:56px;height:56px;border-radius:50%;background:var(--coral);display:flex;align-items:center;justify-content:center}
.testi-title{left:560px;top:2960px;font-size:34px;font-weight:700}
.quote{font-size:110px;font-weight:900;color:#b4362a;line-height:1}
.testi-copy{left:560px;top:3100px;width:500px}
.testi-name{left:560px;top:3210px;font-size:14px;color:var(--coral);line-height:22px}
.dot{width:22px;height:22px;border-radius:50%;background:#c23a2b;left:1116px}

/* footer */
.footer{left:0;top:3380px;width:1200px;height:280px;background:linear-gradient(180deg,var(--coral-soft),var(--coral));color:var(--white)}
.footer h5{font-size:14px;font-weight:700;margin-bottom:14px}
.footer li{list-style:none;font-size:12px;line-height:24px}
.f-brand{left:510px;top:50px;display:flex;align-items:center;gap:12px}
.f-brand .brand-mark{background:var(--white)}
.f-brand .brand-name{color:var(--white)}
.contact{left:830px;top:40px}
.contact div{display:flex;align-items:center;gap:12px;font-size:12px;margin-bottom:18px}
.contact svg{width:20px;height:20px}
.f-rule{left:0;top:220px;width:1200px;height:1px;background:rgba(255,255,255,.4)}
.f-base{top:236px;font-size:11px;color:rgba(255,255,255,.85)}
.social{left:560px;top:232px;display:flex;gap:12px}
.social span{width:18px;height:18px;border-radius:50%;background:var(--white)}
</style>
</head>
<body>

<svg class="abs hero-blob" viewBox="0 0 780 560" aria-hidden="true">
  <defs><linearGradient id="hb" x1="0" y1="0" x2="1" y2="1"><stop offset="0" stop-color="#ff9a7a"/><stop offset="1" stop-color="#f7624f"/></linearGradient></defs>
  <path d="M120 0 H780 V480 C700 540 620 470 560 420 C480 350 400 360 330 300 C250 230 260 140 180 90 C140 60 110 30 120 0Z" fill="url(#hb)"/>
</svg>

<header>
  <div class="abs brand"><span class="brand-mark"></span><span class="brand-name">Pixel Loft Gigs</span></div>
  <nav class="abs nav"><span>How it works</span><span>Login</span><span>Sign Up</span><span>Company</span><span class="pill">Need Help</span></nav>
</header>

<section>
  <h1 class="abs hero-title">A Freelance<br>Marketplace for<br><span>IT &amp; Digital Contractors</span></h1>
  <p class="abs hero-copy">It will provide a way for companies to take advantage of specialist talent for small periods of time and engage with them on a flexible basis.</p>
  <span class="abs btn hero-btn">Get Started</span>
  <div class="abs hero-art" role="img" aria-label="Isometric illustration of a laptop with a freelancer at work surrounded by cloud and device icons"></div>
</section>

<section>
  <h2 class="abs section-title" style="top:590px">Do you want to be a...</h2>
  <div class="abs roles">
    <div class="role"><div class="role-figure" role="img" aria-label="Illustrated gig worker at a laptop"></div><h3>Gigger</h3><p>Find short remote projects that match your skills, set your own rates and work with teams who need expert help right now.</p></div>
    <div class="role"><div class="role-figure" role="img" aria-label="Illustrated customer with a cap"></div><h3>Customer</h3><p>Post a project, compare proposals from vetted specialists and bring in the exact talent you need for as long as you need.</p></div>
    <div class="role"><div class="role-figure" role="img" aria-label="Illustrated affiliate at a desk"></div><h3>Affiliate</h3><p>Share the platform with your network, refer new clients and giggers, and earn a reward for every successful project.</p></div>
  </div>
</section>

<section>
  <h2 class="abs section-title" style="top:1140px">How it works</h2>

  <div class="abs step" style="left:90px;top:1262px">
    <div class="step-label">Giggers</div>
    <h3>A plateform for the techical &nbsp;team</h3>
    <p class="copy">Create your profile, showcase your skills and get matched with businesses looking for specialists in cloud, software and digital delivery.</p>
    <span class="btn">Gigger, Start Here</span>
  </div>
  <div class="abs step-art" style="left:580px;top:1248px;width:540px;height:300px"><div role="img" aria-label="Illustration of a team meeting around a table with laptops" style="background:linear-gradient(160deg,#f3f4fb,#cfd5f3)"></div></div>

  <div class="abs band"></div>
  <div class="abs step-art" style="left:84px;top:1650px;width:500px;height:300px"><div role="img" aria-label="Illustration of people arranging charts and gears on a large screen" style="background:linear-gradient(160deg,#eef0fb,#b9c0ee)"></div></div>
  <div class="abs step" style="left:660px;top:1640px">
    <div class="step-label">Clients</div>
    <h3>Can filters the proposals &amp; Engage<br>the perfect One.</h3>
    <p class="copy">Review proposals side by side, filter by skill, rate and availability, then engage the specialist who fits your project best.</p>
    <span class="btn">Client, Start Here</span>
  </div>

  <div class="abs step" style="left:90px;top:2072px">
    <div class="step-label">Affiliates</div>
    <h3>Join platform and Refer to Earn</h3>
    <p class="copy">Join in minutes, share your personal link with businesses and tech professionals, and earn with every project that goes live.</p>
    <span class="btn">Refer Now</span>
  </div>
  <div class="abs step-art" style="left:580px;top:2070px;width:540px;height:300px"><div role="img" aria-label="Isometric illustration of connected office blocks and people" style="background:linear-gradient(160deg,#f3f4fb,#c6cdf2)"></div></div>
</section>

<section class="abs stats">
  <div class="stat">
    <svg viewBox="0 0 240 240" aria-hidden="true"><circle cx="120" cy="120" r="114" fill="none" stroke="var(--ring)" stroke-width="2"/><circle cx="120" cy="120" r="92" fill="none" stroke="var(--orange)" stroke-width="24" stroke-dasharray="578 578" transform="rotate(-90 120 120)"/><circle cx="120" cy="120" r="74" fill="#f4f4f6"/><text class="stat-num" x="120" y="136" text-anchor="middle">150</text></svg>
    <h4>People visit website<br>in single day</h4>
  </div>
  <div class="stat">
    <svg viewBox="0 0 240 240" aria-hidden="true"><circle cx="120" cy="120" r="114" fill="none" stroke="var(--ring)" stroke-width="2"/><circle cx="120" cy="120" r="92" fill="none" stroke="#fbd7c0" stroke-width="24"/><circle cx="120" cy="120" r="92" fill="none" stroke="var(--orange)" stroke-width="24" stroke-dasharray="272 578" transform="rotate(-90 120 120)"/><circle cx="120" cy="120" r="74" fill="#f4f4f6"/><text class="stat-num" x="120" y="136" text-anchor="middle">47%</text></svg>
    <h4>Website opens<br>on mobile phone</h4>
  </div>
  <div class="stat">
    <svg viewBox="0 0 240 240" aria-hidden="true"><circle cx="120" cy="120" r="114" fill="none" stroke="var(--ring)" stroke-width="2"/><circle cx="120" cy="120" r="92" fill="none" stroke="#fbd7c0" stroke-width="24"/><circle cx="120" cy="120" r="92" fill="none" stroke="var(--orange)" stroke-width="24" stroke-dasharray="462 578" transform="rotate(-90 120 120)"/><circle cx="120" cy="120" r="74" fill="#f4f4f6"/><text class="stat-num" x="120" y="136" text-anchor="middle">80%</text></svg>
    <h4>Visitors are happy<br>with website &amp; their service</h4>
  </div>
</section>

<section>
  <div class="abs testi-band"></div>
  <div class="abs testi-photo" role="img" aria-label="Video still of business people shaking hands in an office"></div>
  <div class="abs play"><svg width="20" height="22" viewBox="0 0 20 22" aria-hidden="true"><path d="M3 2 L18 11 L3 20Z" fill="#fff"/></svg></div>
  <h2 class="abs testi-title">Testimonial</h2>
  <div class="abs quote" style="left:556px;top:3010px">“</div>
  <p class="abs copy testi-copy">There are many variations of passages of text available, but the majority have been altered in some form. We found our cloud specialist within two days and the project shipped on time.</p>
  <div class="abs testi-name">Mr Harlow<br>Australia</div>
  <div class="abs quote" style="left:556px;top:3250px">”</div>
  <span class="abs dot" style="top:3108px"></span>
  <span class="abs dot" style="top:3144px"></span>
</section>

<footer class="abs footer">
  <div class="abs" style="left:80px;top:40px">
    <h5>MAIN LINKS</h5>
    <ul><li>How it works</li><li>Login</li><li>Sign Up</li><li>Company</li></ul>
  </div>
  <div class="abs" style="left:400px;top:30px;width:1px;height:160px;background:rgba(255,255,255,.4)"></div>
  <div class="abs f-brand"><span class="brand-mark"></span><span class="brand-name">Pixel Loft Gigs</span></div>
  <div class="abs" style="left:790px;top:30px;width:1px;height:160px;background:rgba(255,255,255,.4)"></div>
  <div class="abs contact">
    <div><svg viewBox="0 0 20 20" aria-hidden="true"><path d="M5 2 L8 2 L9 6 L7 8 C8 11 9 12 12 13 L14 11 L18 12 L18 15 C18 17 16 18 14 18 C8 17 3 12 2 6 C2 4 3 2 5 2Z" fill="#fff"/></svg>(02) 5550 1842</div>
    <div><svg viewBox="0 0 20 20" aria-hidden="true"><rect x="2" y="4" width="16" height="12" rx="2" fill="none" stroke="#fff" stroke-width="2"/><path d="M3 5 L10 11 L17 5" fill="none" stroke="#fff" stroke-width="2"/></svg>hello@pixelloftgigs.example</div>
    <div><svg viewBox="0 0 20 20" aria-hidden="true"><path d="M10 1 C6 1 4 4 4 7 C4 12 10 19 10 19 C10 19 16 12 16 7 C16 4 14 1 10 1Z" fill="#fff"/><circle cx="10" cy="7" r="2.5" fill="var(--coral)"/></svg>14 Loft Lane, Harbourside</div>
  </div>
  <div class="abs f-rule"></div>
  <div class="abs f-base" style="left:80px">Privacy Policy &nbsp;&nbsp;&nbsp; Terms &amp; Conditions &nbsp;&nbsp;&nbsp; Cookie Settings</div>
  <div class="abs social"><span></span><span></span><span></span></div>
  <div class="abs f-base" style="right:80px">© Pixel Loft Gigs. All rights reserved.</div>
</footer>

</body>
</html>
```